Flyer für Alpaka und Lama Hof
Zielgruppe
Landwirtschaftlicher Betrieb mit Alpakahaltung seit 2021.
Wir bieten an
Alpaka- und LamaWanderungen,
Picknick mit Alpakas und Lamas
Schnupperstunden / Kennenlernen
Betriebsausflüge & Gruppenangebote
Junggesellenabschiede
Persönlich geführt, familiär, mit viel Herzblut und echter Begeisterung für Alpakas und Lamas
Familien, Paare, Betriebe & Teams, Freundesgruppen, Junggesellenabschiede
Tier- & Naturliebhaber,
Menschen, die Alpakas/Lamas lieben oder kennenlernen möchten
Aufgabenstellung
Ziel ist die Gestaltung eines Flyers für ein Alpaka-/Lama Angebot (z. B. Wanderungen, Begegnungen, Erlebnisse), der emotional anspricht, Vertrauen schafft und Lust auf ein besonderes Natur- und Tiererlebnis macht.
Der Flyer kann sich am bestehenden Flyer sowie am Design der Visitenkarten und Gutscheine (mit hochgeladen)orientieren, ohne diese exakt zu kopieren. Der Flyer soll ein 6-seitiger Wickelfalz sein.
Die Texte in meinem hochgeladenen Flyer sind Bausteine und unvollständig. Sie müssen nicht unbedingt verwendet werden und dürfen angepasst werden. Im Flyer soll klar kommuniziert werden, dass alle Alpaka-/Lama Erlebnisse auch als Gutscheine erhältlich sind aber ohne werbliche Sprache.
Ich bin für Text Änderungen offen.

```html
<!DOCTYPE html>
<html lang="de">
<head>
<meta charset="utf-8">
<title>Alpakas vom Lindenhang – Flyer Innenseite</title>
<link href="https://fonts.googleapis.com/css2?family=Montserrat:ital,wght@0,300;0,400;0,500;1,300&display=swap" rel="stylesheet">
<style>
  :root {
    --sand: #c4b59a;
    --earth: #4a3a22;
    --ink: #3b3124;
    --sage: #cfe0a8;
    --cream: #ffffff;
    --photo-forest: linear-gradient(160deg, #5d6b3a 0%, #7d7a55 45%, #8a7a62 75%, #d9cdb8 100%);
    --photo-meadow: linear-gradient(150deg, #6f7d4c 0%, #a99a7f 40%, #c9b79c 65%, #5a6a3c 100%);
  }
  * { box-sizing: border-box; margin: 0; padding: 0; }
  html, body { width: 1200px; height: 805px; overflow: hidden; }
  body { font-family: "Montserrat", sans-serif; color: var(--ink); background: var(--sand); }
  .spread { position: relative; width: 1200px; height: 805px; background: var(--sand); overflow: hidden; }

  .panel-offers { position: absolute; left: 404px; top: 0; width: 403px; height: 805px; background: var(--earth); }

  .url-bar { position: absolute; left: 0; top: 39px; width: 388px; height: 19px; background: var(--earth);
    color: #d8ccb6; font-size: 10.5px; font-weight: 300; text-align: right; padding-right: 6px; line-height: 19px; }

  .heading { position: absolute; font-size: 18.5px; font-weight: 400; letter-spacing: 0.2px; }
  .heading-magic { left: 31px; top: 94px; color: var(--cream); }
  .heading-offers { left: 428px; top: 94px; color: var(--cream); }

  .intro-frame { position: absolute; left: 35px; top: 128px; width: 315px; height: 556px; border: 1.5px solid var(--sage); }
  .intro-text { position: absolute; left: 47px; top: 138px; width: 285px; font-size: 13px; font-weight: 400;
    line-height: 16.4px; text-align: justify; hyphens: manual; color: var(--ink); }
  .intro-text p + p { margin-top: 16px; }

  .photo { position: absolute; }
  .photo-walk { left: 104px; top: 451px; width: 289px; height: 332px; background: var(--photo-forest);
    box-shadow: 3px 3px 6px rgba(0,0,0,0.25); }
  .photo-portrait { left: 866px; top: 163px; width: 285px; height: 415px; background: var(--photo-meadow);
    box-shadow: 3px 3px 6px rgba(0,0,0,0.25); }

  .offer-frame { position: absolute; left: 455px; top: 128px; width: 719px; height: 621px; border: 1.5px solid var(--sage); }

  .offer { position: absolute; left: 430px; width: 360px; }
  .offer-icon { position: absolute; left: 0; width: 50px; height: 50px; border-radius: 50%;
    border: 1.5px solid var(--sage); background: var(--earth); }
  .offer-icon svg { width: 50px; height: 50px; display: block; }
  .offer-body { position: absolute; left: 67px; width: 286px; color: var(--cream); }
  .offer-title { font-size: 13.2px; font-weight: 400; line-height: 16.5px; }
  .offer-text { font-size: 12.4px; font-weight: 300; line-height: 16.3px; text-align: justify; letter-spacing: 0.2px; }

  .voucher-badge { position: absolute; left: 787px; top: 28px; width: 154px; height: 154px; border-radius: 50%;
    background: var(--sand); border: 2.5px solid var(--earth); color: var(--cream);
    display: flex; align-items: center; justify-content: center; text-align: center;
    font-size: 16px; line-height: 19.5px; font-weight: 400; }

  .quote { position: absolute; left: 859px; top: 598px; width: 300px; text-align: center; color: var(--cream);
    font-size: 22px; line-height: 26px; font-weight: 400; }
  .quote-source { position: absolute; right: 49px; top: 708px; color: var(--cream);
    font-size: 11px; font-style: italic; font-weight: 300; }
</style>
</head>
<body>
<main class="spread">
  <div class="panel-offers"></div>

  <div class="url-bar">www.alpakas-vom-lindenhang.de</div>

  <h2 class="heading heading-magic">Die Magie der Alpakas</h2>
  <div class="intro-frame"></div>
  <div class="intro-text">
    <p>Alpakas begeistern mit ihrer sanften, ru&shy;higen Art und ihrem liebenswerten Cha&shy;rakter. Ihre Gelassenheit lädt dazu ein, bewusst langsamer zu werden und den Moment zu genießen. Wer Zeit mit ihnen verbringt, spürt schnell, wie Alltagsstress nachlässt und innere Ruhe einkehrt.</p>
    <p>Diese feinfühligen Tiere strahlen beson&shy;dere Harmonie aus. Sie sind aufmerksam, freundlich und zurückhaltend – eine wohl&shy;tuende Mischung, die Nähe schenkt, ohne aufdringlich zu sein. Zeit mit Alpakas be&shy;deutet Entspannung, Freude und eine kleine Auszeit für die Seele. Ob beim Beob&shy;achten, Spaziergang oder Innehalten – sie helfen, neue Energie zu tanken und dem Alltag kurz zu entfliehen.</p>
  </div>
  <div class="photo photo-walk" role="img" aria-label="Foto: ein schwarz-weißes Lama und ein helles Alpaka am Halfter auf einem Waldweg"></div>

  <h2 class="heading heading-offers">Erleben statt nur besuchen</h2>
  <div class="offer-frame"></div>

  <div class="offer" style="top:140px">
    <div class="offer-icon"><svg viewBox="0 0 50 50" fill="none" stroke="#fff" stroke-width="1.4" stroke-linecap="round"><path d="M17 34 L23 26 L27 30 L33 18"/><path d="M29 18 H33 V22"/><circle cx="17" cy="34" r="1.5"/></svg></div>
    <div class="offer-body" style="top:0"><div class="offer-title">Alpaka- und Lama Wanderungen</div><div class="offer-text">exklusiv im kleinen Kreis oder gemeinsam in der Gruppe</div></div>
  </div>

  <div class="offer" style="top:222px">
    <div class="offer-icon"><svg viewBox="0 0 50 50" fill="none" stroke="#fff" stroke-width="1.4" stroke-linejoin="round"><path d="M15 22 H35 L33 34 H17 Z"/><path d="M18 22 C18 14 32 14 32 22"/><path d="M16 27 H34"/></svg></div>
    <div class="offer-body" style="top:-3px"><div class="offer-title">Picknick mit Alpakas und Lamas</div><div class="offer-text">naturnah, barrierefrei und für alle Altersgruppen geeignet</div></div>
  </div>

  <div class="offer" style="top:288px">
    <div class="offer-icon"><svg viewBox="0 0 50 50" fill="none" stroke="#fff" stroke-width="1.4" stroke-linecap="round"><path d="M18 16 L20 22 M32 16 L30 22"/><path d="M19 22 C17 30 19 36 25 36 C31 36 33 30 31 22 Z"/></svg></div>
    <div class="offer-body" style="top:16px"><div class="offer-title">Schnupperstunden &amp; Kennenlernen</div><div class="offer-text">um die Welt der Alpakas kennenzulernen</div></div>
  </div>

  <div class="offer" style="top:364px">
    <div class="offer-icon"><svg viewBox="0 0 50 50" fill="#fff"><ellipse cx="22" cy="20" rx="3" ry="4.5" transform="rotate(-25 22 20)"/><ellipse cx="30" cy="24" rx="3" ry="4.5" transform="rotate(-25 30 24)"/><ellipse cx="19" cy="31" rx="3" ry="4.5" transform="rotate(-25 19 31)"/><ellipse cx="27" cy="35" rx="3" ry="4.5" transform="rotate(-25 27 35)"/></svg></div>
    <div class="offer-body" style="top:4px"><div class="offer-title">Betriebsausflüge &amp; Gruppenangebote</div><div class="offer-text">Teambuilding und Abenteuer in der Natur für effektive Zusammenarbeit</div></div>
  </div>

  <div class="offer" style="top:446px">
    <div class="offer-icon"><svg viewBox="0 0 50 50" fill="none" stroke="#fff" stroke-width="1.4" stroke-linecap="round"><path d="M17 15 L21 15 L20 25 C20 27 18 27 18 25 Z M19 27 L19 35 M16 35 H22"/><path d="M29 15 L33 15 L32 25 C32 27 30 27 30 25 Z M31 27 L31 35 M28 35 H34"/></svg></div>
    <div class="offer-body" style="top:-2px"><div class="offer-title">Junggesellenabschiede</div><div class="offer-text">die bewusst anders sind und lange in Erinnerung bleiben</div></div>
  </div>

  <div class="offer" style="top:527px">
    <div class="offer-icon"><svg viewBox="0 0 50 50" fill="none" stroke="#fff" stroke-width="1.4" stroke-linejoin="round"><path d="M14 19 H20 L22 16 H28 L30 19 H36 V34 H14 Z"/><circle cx="25" cy="26.5" r="5"/></svg></div>
    <div class="offer-body" style="top:-1px"><div class="offer-title">Shootings</div><div class="offer-text">mit tierischer Begleitung in einzigartiger Kulisse</div></div>
  </div>

  <div class="offer" style="top:609px">
    <div class="offer-icon"><svg viewBox="0 0 50 50" fill="none" stroke="#fff" stroke-width="1.4" stroke-linejoin="round"><path d="M25 31 C17 25 18 19 22 19 C24 19 25 21 25 21 C25 21 26 19 28 19 C32 19 33 25 25 31 Z"/><path d="M14 24 L17 34 L22 37 M36 24 L33 34 L28 37"/></svg></div>
    <div class="offer-body" style="top:-1px"><div class="offer-title">Tierpatenschaften</div><div class="offer-text">schenken Nähe, Verantwortung und das gute Gefühl, Teil unseres Hoflebens zu sein</div></div>
  </div>

  <div class="voucher-badge">Alle Erlebnisse<br>können auch<br>als Gutschein<br>verschenkt<br>werden!</div>

  <div class="photo photo-portrait" role="img" aria-label="Foto: zwei helle Alpakas im Profil vor einer grünen Weide"></div>

  <blockquote class="quote">„Schau einem Alpaka nicht zu tief in die Augen, du könntest dich verlieben.“</blockquote>
  <div class="quote-source">altes peruanisches Sprichwort</div>
</main>
</body>
</html>
```